Stationary Design for Health Service Company
A digital Initiative
Stationary Design for Health Service Company - Health
Creative Brief
Professional
Harjeet Malhan
Managing Director
CORALPEAK Health Services PVT LTD 27/3 Parvati Road West, 2nd Lane, Behala, Kolkata 700061
harjeet@vitanova.example.in
www.vitanova.example.in
Please read the project document attached in the project files. The final design must be transferred on the PSD and AI template provided. The Letterhead needs to be in WORD document and also in PSD & AI. All items must have 2 logos - Vitanova and CORALPEAK Health Services. For the CORALPEAK logo provided, please change the text from "Network Solutions" to "Health Services"
The back of the business card must have only one logo - CORALPEAK Health Service

```html
<!DOCTYPE html>
<html lang="en">
<head>
<meta charset="utf-8">
<title>Vitanova &amp; CORALPEAK Business Cards</title>
<link rel="stylesheet" href="https://fonts.googleapis.com/css2?family=Montserrat:wght@400;600&display=swap">
<style>
  :root {
    --backdrop: #3a3a3c;
    --card-white: #ffffff;
    --card-shade: #f1f1f1;
    --ink-dark: #1e1e20;
    --ink-muted: #555559;
    --brand-blue: #1f7ecb;
    --panel-black: #1b1b1d;
    --contact-ink: #e8e8ea;
  }
  * { margin: 0; padding: 0; box-sizing: border-box; }
  html, body {
    width: 1200px; height: 670px; overflow: hidden;
    background: var(--backdrop);
    font-family: "Montserrat", sans-serif;
  }
  .stage { position: relative; width: 1200px; height: 670px; }
  .card {
    position: absolute; width: 520px; height: 297px;
    background: linear-gradient(160deg, var(--card-white) 60%, var(--card-shade));
    box-shadow: 0 14px 30px rgba(0,0,0,.45);
    overflow: hidden;
  }
  .card--front { left: 50px; top: 120px; }
  .card--back { left: 630px; top: 250px; }

  .front-logo {
    position: absolute; inset: 0;
    display: flex; align-items: center; justify-content: center;
  }
  .front-logo__name {
    font-weight: 600; font-size: 40px; color: var(--ink-dark);
  }

  .back-art { position: absolute; inset: 0; }

  .back-logo {
    position: absolute; left: 36px; top: 96px;
    font-weight: 600; font-size: 20px; line-height: 1.2; color: var(--ink-dark);
  }

  .holder { position: absolute; left: 60px; top: 176px; }
  .holder__name {
    font-weight: 600; font-size: 14px; color: var(--ink-dark);
    text-transform: uppercase; letter-spacing: .5px;
  }
  .holder__title { font-weight: 400; font-size: 10px; color: var(--ink-muted); margin-top: 3px; }

  .contact {
    position: absolute; right: 22px; top: 36px; width: 170px;
    font-style: normal; color: var(--contact-ink);
    font-size: 7.5px; line-height: 1.45; text-align: right;
  }
  .contact__address { margin-bottom: 14px; }
  .contact__row { display: flex; justify-content: flex-end; align-items: center; gap: 6px; margin-bottom: 3px; }
  .contact__icon { width: 8px; height: 8px; flex: none; }
  .contact__links { margin-top: 16px; }
</style>
</head>
<body>
<main class="stage">

  <section class="card card--front" aria-label="Business card front">
    <div class="front-logo">
      <span class="front-logo__name">Vitanova</span>
    </div>
  </section>

  <section class="card card--back" aria-label="Business card back">
    <svg class="back-art" viewBox="0 0 520 297" preserveAspectRatio="none" aria-hidden="true">
      <path d="M330 0 C 250 60, 300 150, 240 220 C 200 262, 120 262, 0 262 L0 297 L520 297 L520 0 Z" fill="var(--brand-blue)"/>
      <path d="M345 0 C 270 60, 315 150, 255 226 C 215 272, 130 272, 0 272 L0 297 L520 297 L520 0 Z" fill="var(--panel-black)"/>
    </svg>

    <div class="back-logo">CORALPEAK<br>Health Services</div>

    <div class="holder">
      <div class="holder__name">Harjeet Malhan</div>
      <div class="holder__title">Managing Director</div>
    </div>

    <address class="contact">
      <div class="contact__address">27/3 Parvati Road West, 2nd Lane,<br>Behala, Kolkata 700061</div>
      <div class="contact__row"><span>033 240 0100</span>
        <svg class="contact__icon" viewBox="0 0 10 10"><path d="M2 1h2l1 2-1.2 1a5 5 0 0 0 2.2 2.2L7 5l2 1v2a1 1 0 0 1-1 1A7 7 0 0 1 1 2a1 1 0 0 1 1-1z" fill="currentColor"/></svg></div>
      <div class="contact__row"><span>033 240 0101</span>
        <svg class="contact__icon" viewBox="0 0 10 10"><path d="M2 1h2l1 2-1.2 1a5 5 0 0 0 2.2 2.2L7 5l2 1v2a1 1 0 0 1-1 1A7 7 0 0 1 1 2a1 1 0 0 1 1-1z" fill="currentColor"/></svg></div>
      <div class="contact__row"><span>033 240 0102</span>
        <svg class="contact__icon" viewBox="0 0 10 10"><path d="M2 1h2l1 2-1.2 1a5 5 0 0 0 2.2 2.2L7 5l2 1v2a1 1 0 0 1-1 1A7 7 0 0 1 1 2a1 1 0 0 1 1-1z" fill="currentColor"/></svg></div>
      <div class="contact__links">
        <div>harjeet@vitanova.example.in</div>
        <div>www.vitanova.example.in</div>
      </div>
    </address>
  </section>

</main>
</body>
</html>
```